Flyer Design

we are cleaning company specialize in home cleaning, based in North Shore in Auckland (NZ).
Company name RW is initial of bright wren.
we provide professional, high standard,attention to detail service,
to make dust-free, sparkling house and no-stress family.

(business practice)--don't write this title
"colour coded cleaning system"
---we use different colour's microfiber cloths and mop heads for more hygene.
"green and clean"
---we use eco-friendly, non-toxic cleaning products for environment and your family's health.

service we offer
regular cleaning service
--weekly, fortnightly, monthly
one-off cleaning service
---move in/out cleaning
---rental inspection cleaning
---spring cleaning
---open home cleaning
---remodeling clean-up
---special occasion cleaning(event,party)

special cleaning
---window cleaning
---oven cleaning
---house washing(water blasting)

Free in home no obligation consultation and 50% off first service.
contact no; Rob and Helen 021 0487 5620,09-561-2047
e-mail info@rwcleaning.example.nz
www.rwcleaning.example.nz

we would like to see designs that use colours blue and lite pink, clean, bright and friendly image.

Target Market(s)

Woman aged between late 30th to 60th, housewives, career woman, senior etc.

Industry/Entity Type

Environment

Requirements
Should not have
• For the introduction instead of writing what I have written above verbatim, would you be able to go to our website and paraphrase/reword the introduction that's already there?

Also please don't use the picture on the website, we are planning to change the picture. Thanks.

```html
<!DOCTYPE html>
<html lang="en">
<head>
<meta charset="utf-8">
<title>RW Cleaning Flyer</title>
<link rel="stylesheet" href="https://fonts.googleapis.com/css2?family=Raleway:wght@400;500;600;700&display=swap">
<style>
  :root {
    --paper: #f3f3ef;
    --grid: rgba(150, 150, 190, 0.22);
    --ink-blue: #2a7ea6;
    --ink-dark: #1f6f95;
    --sun: #f2c41a;
    --band: #2585ad;
    --white: #ffffff;
    --leaf: #2f8f3f;
    --petal: #f1d43c;
  }
  * { margin: 0; padding: 0; box-sizing: border-box; }
  html, body { width: 1200px; height: 900px; overflow: hidden; }
  body { font-family: "Raleway", sans-serif; background: var(--paper); }

  .flyer {
    position: relative;
    width: 1200px;
    height: 900px;
    background-color: var(--paper);
    background-image:
      linear-gradient(var(--grid) 1px, transparent 1px),
      linear-gradient(90deg, var(--grid) 1px, transparent 1px);
    background-size: 25px 25px;
    background-position: 8px 8px;
    overflow: hidden;
  }

  .floral-spray {
    position: absolute;
    left: 685px;
    top: 35px;
    width: 480px;
    height: 220px;
    border-radius: 50% 40% 45% 55%;
    background:
      radial-gradient(ellipse at 40% 55%, rgba(242, 200, 40, 0.55), transparent 60%),
      radial-gradient(ellipse at 70% 40%, rgba(47, 143, 63, 0.55), transparent 62%),
      radial-gradient(ellipse at 25% 30%, rgba(200, 90, 170, 0.3), transparent 55%);
  }

  .intro {
    position: absolute;
    left: 68px;
    top: 58px;
    width: 620px;
    font-size: 20px;
    line-height: 26.5px;
    color: var(--ink-blue);
  }
  .intro strong { color: var(--ink-dark); font-weight: 700; }

  .section-title {
    position: absolute;
    font-size: 23px;
    font-weight: 500;
    color: var(--sun);
  }
  .practice-title { left: 68px; top: 215px; }
  .services-title { left: 68px; top: 390px; }
  .special-title { left: 537px; top: 388px; }

  .practice {
    position: absolute;
    left: 72px;
    top: 257px;
    color: var(--ink-blue);
    font-size: 19px;
    line-height: 26.5px;
  }
  .practice-name { font-weight: 700; color: var(--ink-dark); }

  .service-list {
    position: absolute;
    list-style: none;
    font-size: 19px;
    line-height: 25.2px;
    color: var(--ink-blue);
  }
  .service-list li { position: relative; padding-left: 14px; }
  .service-list li::before {
    content: "";
    position: absolute;
    left: -6px;
    top: 11px;
    width: 6px;
    height: 6px;
    border-radius: 50%;
    background: var(--sun);
  }
  .services { left: 68px; top: 430px; }
  .special { left: 536px; top: 430px; }

  .contact-band {
    position: absolute;
    left: 0;
    top: 690px;
    width: 1200px;
    height: 210px;
    background: var(--band);
    color: var(--white);
    text-align: center;
    font-size: 18px;
    line-height: 25.5px;
    padding-top: 34px;
  }
  .contact-band strong { font-weight: 600; }
</style>
</head>
<body>
<main class="flyer">
  <div class="floral-spray" role="img" aria-label="Illustration of colourful flowers and leaves bursting from a green spray bottle"></div>

  <p class="intro">
    We are cleaning company specialize in home cleaning, based<br>
    in <strong>North Shore in Auckland (NZ).</strong>Company name RW is initial of<br>
    bright wren.we provide <strong>professional, high standard, attention</strong> to<br>
    detail service,to make <strong>dust-free, sparkling house</strong> and <strong>no<br>
    stress family</strong>.
  </p>

  <h2 class="section-title practice-title">Business Practice</h2>
  <div class="practice">
    <p class="practice-name">"Color Coded Cleaning System"</p>
    <p>we use different color's microfiber cloths and mop heads for more hygiene.</p>
    <p class="practice-name">"Green and Clean"</p>
    <p>we use eco-friendly, non-toxic cleaning for environment and your family's health.</p>
  </div>

  <h2 class="section-title services-title">Service we offer</h2>
  <ul class="service-list services">
    <li>regular cleaning service</li>
    <li>weekly, fortnightly, monthly</li>
    <li>one-off cleaning service</li>
    <li>move in/out cleaning</li>
    <li>rental inspection cleaning</li>
    <li>spring cleaning</li>
    <li>open home cleaning</li>
    <li>remodeling clean-up</li>
    <li>special occasion cleaning(event, party)</li>
  </ul>

  <h2 class="section-title special-title">Special Cleaning</h2>
  <ul class="service-list special">
    <li>window cleaning</li>
    <li>oven cleaning</li>
    <li>house washing (water blasting)</li>
  </ul>

  <footer class="contact-band">
    <p><strong>Free in home no obligation consultation and 50% off first service.</strong></p>
    <p><strong>Contact no:</strong> Rob and Helen 021 0487 5620,09-561-2047</p>
    <p><strong>E-mail:</strong> info@rwcleaning.example.nz</p>
    <p>www.rwcleaning.example.nz</p>
  </footer>
</main>
</body>
</html>
```